Express envelope design for courier company

We're a courier company launching a new service for sending documents around Australia. We need a design for the express envelope that will be used to hold the documents during transit. The envelope will be printed in colour on cardboard. Please see brief attached.

Design cues:
• Vibrant
• Simplified
• Clean
• Aesthetically pleasing
• Artistic
• Nothing “institutional” or “Harwick Lines”
• Nothing cramped, no small text

It's fine to crop, recolour, or reinterpret the logo.

Industry/Entity Type

It Company

Font styles to use
Sans Serif

Requirements
Must have
• Dimensions:
• Back side: 350 x 230 mm
• Front side: 387.5 x 230 mm (including flap to close envelope)
• Back side barcode panel: 90 x 75 mm (blank area for adhesive barcode)
• Back side address panel: 150 x 90 mm (see PDF for contents and layout)
• Front side text:
• QM-DR
• Express Envelope
• Send With Trust
• 1300 584 961
• qmdr.com.au
• Back side text:
• For documents
• Max. weight 500g, max width 20mm
• Send With Trust
• • Time-guaranteed and next-flight-out service for vital deliveries
• • Same-day and next-day local services
• • Overnight service to most Australian locations
• • Budget road service Australia-wide
• • Worldwide express courier
• Visit qmdr.com.au or phone 1300 584 961
• Flap text:
• Go to qmdr.com.au to book your pickup.
• Carried subject to QM-DR Standard Conditions of Carriage; see our website.
Nice to have
• Our web colours:
• #fcd614
• #d06517
• #3b5274
• #f0f0d8
• #382a3a

```html
<!DOCTYPE html>
<html lang="en">
<head>
<meta charset="utf-8">
<title>QM-DR Express Envelope</title>
<link rel="stylesheet" href="https://fonts.googleapis.com/css2?family=Archivo:ital,wght@0,400;0,700;0,900;1,700&display=swap">
<style>
  :root {
    --blue: #21468f;
    --yellow: #f8dc1a;
    --orange: #d24a10;
    --cream: #f0f0d8;
    --white: #ffffff;
  }
  * { margin: 0; padding: 0; box-sizing: border-box; }
  html, body { width: 1200px; height: 712px; overflow: hidden; background: var(--blue); }
  .envelope {
    position: relative;
    width: 1200px;
    height: 712px;
    background: var(--blue);
    font-family: "Archivo", Arial, sans-serif;
    color: var(--white);
    overflow: hidden;
  }
  .shapes { position: absolute; inset: 0; }
  .brand {
    position: absolute;
    left: 122px;
    top: 294px;
    width: 360px;
  }
  .brand-name {
    font-weight: 900;
    font-size: 84px;
    line-height: 1;
    color: var(--yellow);
    letter-spacing: 2px;
  }
  .brand-product {
    margin-top: 6px;
    font-weight: 700;
    font-style: italic;
    font-size: 26px;
    letter-spacing: 5.6px;
    color: var(--white);
    white-space: nowrap;
  }
  .flap-note {
    position: absolute;
    right: 42px;
    top: 44px;
    text-align: right;
    font-size: 15.5px;
    line-height: 21px;
    white-space: nowrap;
  }
  .flap-note .url { color: var(--yellow); font-size: 19px; }
  .features {
    position: absolute;
    left: 614px;
    top: 286px;
    display: flex;
    gap: 28px;
  }
  .feature { width: 118px; text-align: center; font-size: 13px; letter-spacing: 0.3px; }
  .feature svg { display: block; margin: 0 auto 8px; }
  .feature--sending { color: var(--orange); }
  .feature--documents { color: var(--yellow); }
  .feature--australia { color: var(--white); }
  .contact {
    position: absolute;
    right: 40px;
    top: 535px;
    text-align: right;
    font-size: 19px;
    line-height: 25px;
  }
  .footer-name {
    position: absolute;
    right: 224px;
    top: 598px;
    font-weight: 900;
    font-size: 38px;
    line-height: 1;
    color: var(--white);
  }
</style>
</head>
<body>
<main class="envelope">
  <svg class="shapes" width="1200" height="712" viewBox="0 0 1200 712" aria-hidden="true">
    <polygon points="0,0 205,0 376,272 0,272" fill="var(--yellow)"/>
    <polygon points="205,0 352,0 278,116" fill="var(--orange)"/>
    <polygon points="150,423 472,423 650,712 150,712" fill="var(--yellow)"/>
  </svg>

  <div class="brand">
    <div class="brand-name">QM-DR</div>
    <div class="brand-product">Express Envelope</div>
  </div>

  <p class="flap-note">
    Go to <span class="url">qmdr.com.au</span> to book your pickup.<br>
    Carried subject to QM-DR Standard Conditions of Carriage; see our website
  </p>

  <div class="features">
    <div class="feature feature--sending">
      <svg width="118" height="118" viewBox="0 0 118 118" aria-hidden="true">
        <circle cx="59" cy="59" r="56" fill="none" stroke="var(--orange)" stroke-width="4"/>
        <circle cx="59" cy="59" r="46" fill="none" stroke="var(--orange)" stroke-width="3"/>
        <polygon points="28,62 90,32 60,90 56,68" fill="var(--orange)"/>
      </svg>
      SENDING
    </div>
    <div class="feature feature--documents">
      <svg width="118" height="118" viewBox="0 0 118 118" aria-hidden="true">
        <circle cx="59" cy="59" r="56" fill="none" stroke="var(--yellow)" stroke-width="4"/>
        <circle cx="59" cy="59" r="46" fill="none" stroke="var(--yellow)" stroke-width="3"/>
        <rect x="40" y="32" width="34" height="46" rx="3" fill="none" stroke="var(--yellow)" stroke-width="3"/>
        <rect x="46" y="38" width="34" height="46" rx="3" fill="var(--blue)" stroke="var(--yellow)" stroke-width="3"/>
        <g stroke="var(--yellow)" stroke-width="2.5">
          <line x1="53" y1="50" x2="73" y2="50"/>
          <line x1="53" y1="57" x2="73" y2="57"/>
          <line x1="53" y1="64" x2="73" y2="64"/>
          <line x1="53" y1="71" x2="73" y2="71"/>
        </g>
      </svg>
      DOCUMENTS
    </div>
    <div class="feature feature--australia">
      <svg width="118" height="118" viewBox="0 0 118 118">
        <circle cx="59" cy="59" r="56" fill="none" stroke="var(--white)" stroke-width="4"/>
        <circle cx="59" cy="59" r="46" fill="none" stroke="var(--white)" stroke-width="3"/>
        <circle cx="59" cy="59" r="30" fill="var(--cream)" role="img" aria-label="Map of Australia"/>
      </svg>
      AUSTRALIA
    </div>
  </div>

  <p class="contact">1300 584 961<br>qmdr.com.au</p>

  <div class="footer-name">QM-DR</div>
</main>
</body>
</html>
```